Business Card - Harlow Birch

Need Business Card design for company named Harlow Birch. Software development focused mainly on Ardel eKallo & oBix Apps. I've attached our logo with both a black and white background. Please add trademark symbol to logo when using.

```html
<!DOCTYPE html>
<html lang="en">
<head>
<meta charset="utf-8">
<title>Harlow Birch – Business Card</title>
<link rel="stylesheet" href="https://fonts.googleapis.com/css2?family=Exo+2:wght@600&family=Source+Code+Pro:wght@400&display=swap">
<style>
  :root {
    --canvas-bg: #e6e3df;
    --card-dark: #2a2a2b;
    --card-light: #ffffff;
    --ink: #1d1d1d;
    --ink-soft: #9a9a9a;
    --line-number: #b9b9b9;
    --brand-yellow: #f2c21a;
    --brand-orange: #f0801e;
    --brand-red: #e2261d;
    --logo-white: #f4f4f4;
    --rule: #cfcfcf;
  }
  * { box-sizing: border-box; margin: 0; padding: 0; }
  html, body { width: 1200px; height: 900px; overflow: hidden; }
  body {
    background: var(--canvas-bg);
    display: flex;
    flex-direction: column;
    align-items: center;
    justify-content: center;
    gap: 48px;
  }
  .card {
    width: 640px;
    height: 366px;
    border-radius: 4px;
    box-shadow: 0 10px 30px rgba(0,0,0,.18);
    position: relative;
    overflow: hidden;
  }

  /* Front */
  .card-front {
    background: var(--card-dark);
    display: flex;
    align-items: center;
    justify-content: center;
  }
  .brand-lockup {
    display: flex;
    align-items: center;
    gap: 18px;
  }
  .brand-dot {
    width: 44px;
    height: 44px;
    border-radius: 50%;
    background: var(--brand-orange);
  }
  .brand-name {
    font-family: "Exo 2", sans-serif;
    font-weight: 600;
    font-size: 52px;
    letter-spacing: -1px;
    color: var(--logo-white);
  }

  /* Back */
  .card-back {
    background: var(--card-light);
    padding: 34px 40px;
  }
  .code-listing {
    font-family: "Source Code Pro", monospace;
    font-size: 15px;
    line-height: 20px;
    color: var(--ink);
    list-style: none;
  }
  .code-line {
    display: flex;
    white-space: pre;
    min-height: 20px;
  }
  .line-number {
    width: 34px;
    color: var(--line-number);
    font-size: 12px;
  }
  .code-var { color: var(--brand-orange); }
  .code-punct { color: var(--ink-soft); }
  .code-key { color: var(--ink-soft); }
  .url-host { color: var(--brand-yellow); }
  .url-domain { color: var(--brand-red); }
  .back-brand {
    position: absolute;
    right: 78px;
    bottom: 34px;
    font-family: "Exo 2", sans-serif;
    font-weight: 600;
    font-size: 30px;
    letter-spacing: -0.5px;
    color: var(--ink);
  }
  .trim-rule-vertical {
    position: absolute;
    right: 40px;
    top: 150px;
    bottom: 20px;
    border-left: 1px dashed var(--rule);
  }
</style>
</head>
<body>

  <section class="card card-front" aria-label="Card front">
    <div class="brand-lockup">
      <span class="brand-dot" aria-hidden="true"></span>
      <span class="brand-name">Harlow Birch™</span>
    </div>
  </section>

  <section class="card card-back" aria-label="Card back">
    <ol class="code-listing">
      <li class="code-line"><span class="line-number">1</span><span class="code-var">hb</span><span class="code-punct"> = {</span></li>
      <li class="code-line"><span class="line-number">2</span></li>
      <li class="code-line"><span class="line-number">3</span><span class="code-key">    "name"    </span><span class="code-punct">: "</span>Milo Varga<span class="code-punct">",</span></li>
      <li class="code-line"><span class="line-number">4</span><span class="code-key">    "email"   </span><span class="code-punct">: "</span>info@harlowbirch.com<span class="code-punct">",</span></li>
      <li class="code-line"><span class="line-number">5</span><span class="code-key">    "mobile"  </span><span class="code-punct">: "</span>555-214-7731<span class="code-punct">",</span></li>
      <li class="code-line"><span class="line-number">6</span><span class="code-key">    "fax"     </span><span class="code-punct">: "</span>555-214-7790<span class="code-punct">",</span></li>
      <li class="code-line"><span class="line-number">7</span><span class="code-key">    "url"     </span><span class="code-punct">: "</span>http://<span class="url-host">www.</span><span class="url-domain">harlowbirch.com</span><span class="code-punct">",</span></li>
      <li class="code-line"><span class="line-number">8</span><span class="code-key">    "address" </span><span class="code-punct">: "</span>2140 Alder Row, Fenwick, FL 33990<span class="code-punct">"</span></li>
      <li class="code-line"><span class="line-number">9</span><span class="code-punct">}</span></li>
      <li class="code-line"><span class="line-number">10</span></li>
      <li class="code-line"><span class="line-number">11</span></li>
      <li class="code-line"><span class="line-number">12</span></li>
      <li class="code-line"><span class="line-number">13</span></li>
      <li class="code-line"><span class="line-number">14</span></li>
    </ol>
    <span class="trim-rule-vertical" aria-hidden="true"></span>
    <span class="back-brand">Harlow Birch™</span>
  </section>

</body>
</html>
```